Brell Harbor Company Business Cards

Front and Back Business Card - logo and text setup - cool design. I need workable photoshop or illustrator files so I can setup each employee card with design that is created
Updates

Hi everyone, thank you for the great entries. Please no more white and blue cards - there are so many already - black and silver only now please. thanks!

Target Market(s)

Construction Industry - Facility Managers

Industry/Entity Type

Construction

Contact Information for Business Card

I really like contemporary simplistic looks - clean neat....not opposed to seeing some black backrounds

Requirements
Must have
• Logo/website address with design on front only - www.brellharbor-example.com (logo attached)
• Back:
• Name/Title/Company Address/Phone/email address
Nice to have
• Cool design
Should not have
• Nothing gimmicky like Fire or Water - since we are a Fire Protection company - it has all been done

```html
<!DOCTYPE html>
<html lang="en">
<head>
<meta charset="utf-8">
<title>Brell Harbor Company Business Cards</title>
<link href="https://fonts.googleapis.com/css2?family=Arimo:wght@400;700&display=swap" rel="stylesheet">
<style>
  :root {
    --backdrop: #dcdde0;
    --card: #121314;
    --silver: #c4c7cc;
    --silver-bright: #eef0f2;
    --steel: #8a8e95;
  }
  * { box-sizing: border-box; margin: 0; padding: 0; }
  html, body {
    width: 1200px;
    height: 880px;
    overflow: hidden;
    background: var(--backdrop);
    font-family: "Arimo", Arial, sans-serif;
  }
  .canvas {
    position: relative;
    width: 1200px;
    height: 880px;
  }
  .card {
    position: absolute;
    width: 520px;
    height: 300px;
    background: var(--card);
    border-radius: 18px;
    overflow: hidden;
    box-shadow: 0 14px 30px rgba(0,0,0,0.35);
  }
  .card--front { left: 80px; top: 110px; }
  .card--back { left: 600px; top: 470px; }

  /* Front */
  .brand {
    position: absolute;
    left: 0; right: 0;
    top: 96px;
    text-align: center;
  }
  .brand__name {
    display: inline-flex;
    align-items: center;
    gap: 12px;
    font-weight: 700;
    font-size: 44px;
    letter-spacing: -1px;
    line-height: 1;
    color: var(--silver-bright);
  }
  .brand__mark {
    width: 16px;
    height: 16px;
    background: var(--steel);
  }
  .brand__web {
    margin-top: 26px;
    font-size: 13px;
    font-weight: 700;
    letter-spacing: 4px;
    color: var(--silver);
  }

  /* Back */
  .accent-block {
    position: absolute;
    right: 0;
    top: 58px;
    width: 56px;
    height: 70px;
    background: var(--silver);
  }
  .contact {
    position: absolute;
    left: 44px;
    bottom: 46px;
    color: var(--silver);
    font-size: 13px;
    line-height: 1.4;
  }
  .contact__name {
    font-weight: 700;
    font-size: 17px;
    letter-spacing: 0.2px;
    color: var(--silver-bright);
  }
  .contact__role {
    color: var(--steel);
    font-size: 15px;
    border-left: 1px solid var(--silver);
    padding-left: 6px;
    margin-left: 6px;
  }
  .contact__row {
    display: flex;
    align-items: center;
    gap: 6px;
  }
  .contact__sep {
    width: 1px;
    height: 14px;
    background: var(--silver);
    margin: 0 4px;
  }
  .contact__icon { width: 12px; height: 12px; flex: none; }
  .contact__web {
    font-size: 13px;
    letter-spacing: 4px;
    padding-bottom: 4px;
    border-bottom: 1.5px solid var(--steel);
    width: 390px;
  }
</style>
</head>
<body>
<main class="canvas">

  <section class="card card--front" aria-label="Card front">
    <div class="brand">
      <div class="brand__name"><span class="brand__mark"></span>Brell Harbor</div>
      <div class="brand__web">www.brellharbor-example.com</div>
    </div>
  </section>

  <section class="card card--back" aria-label="Card back">
    <div class="accent-block"></div>
    <div class="contact">
      <div><span class="contact__name">DARA VELLOWAY</span><span class="contact__role">Director</span></div>
      <div>PO BOX 418, Quay Lane</div>
      <div>4th street, Norvale</div>
      <div class="contact__row">
        <svg class="contact__icon" viewBox="0 0 12 12" aria-hidden="true">
          <rect x="2" y="0.75" width="8" height="10.5" rx="1" fill="none" stroke="var(--steel)" stroke-width="1.5"/>
        </svg>
        <span>(555) 301 2468</span>
        <span class="contact__sep"></span>
        <svg class="contact__icon" viewBox="0 0 12 12" aria-hidden="true">
          <rect x="0.5" y="2" width="11" height="8" fill="var(--steel)"/>
          <path d="M0.5 2 L6 7 L11.5 2" fill="none" stroke="var(--card)" stroke-width="1"/>
        </svg>
        <span>hello@brellmail-example.com</span>
      </div>
      <div class="contact__web">www.brellweb-example.com</div>
    </div>
  </section>

</main>
</body>
</html>
```